Car wrap design for a solar energy installation company - Brightvane

We want a clean looking car wrap design for a solar enerrgy installation company. It must be in our company colours! We want it in bright yellow with black text. Please see attached images for referance and inspiration.

Target Market(s)

Residential consumers

Industry/Entity Type

Renewable energy, solar installations

Font styles to use
Other font styles liked:
• Montserrat semi bold

Colors
FFF300
FFF600
FEFA6F
FFFEC7
FFFEE8

Requirements
Must have
• Copmany name, services & products offered, company colours, easy to read, "bullet points"
Nice to have
• Be creative!
Should not have
• To advanced, to many colours,

```html
<!DOCTYPE html>
<html lang="en">
<head>
<meta charset="utf-8">
<title>Brightvane – Vehicle Wrap Side Layouts</title>
<link rel="stylesheet" href="https://fonts.googleapis.com/css2?family=Montserrat:wght@600;700&family=PT+Sans:wght@400&display=swap">
<style>
  :root {
    --backdrop: #ececec;
    --body-white: #ffffff;
    --body-edge: #d6d6d6;
    --wrap-yellow-soft: #f0d63c;
    --wrap-yellow-bright: #fbe24c;
    --ink: #1a1a1a;
  }
  html, body {
    margin: 0;
    padding: 0;
    width: 1190px;
    height: 1200px;
    overflow: hidden;
    background: var(--backdrop);
  }
  .wrap-sheet {
    display: flex;
    flex-direction: column;
    width: 1190px;
    height: 1200px;
  }
  .wrap-variant {
    display: block;
    width: 1190px;
    height: 600px;
  }
  .vehicle-side { fill: var(--body-white); stroke: var(--body-edge); stroke-width: 2; }
  .variant-soft .wrap-field, .variant-soft .brand-name { fill: var(--wrap-yellow-soft); }
  .variant-bright .wrap-field, .variant-bright .brand-name { fill: var(--wrap-yellow-bright); }
  .brand-name {
    font-family: "Montserrat", sans-serif;
    font-weight: 700;
    font-size: 150px;
  }
  .contact-line {
    font-family: "PT Sans", sans-serif;
    font-size: 14px;
    fill: var(--ink);
  }
  .contact-icon { fill: var(--ink); }
  .contact-icon-mark { stroke: var(--body-white); stroke-width: 1.4; fill: none; }
</style>
</head>
<body>
<main class="wrap-sheet">

  <svg class="wrap-variant variant-soft" viewBox="0 0 1190 600" aria-label="Brightvane van wrap, side view, soft yellow version">
    <defs>
      <clipPath id="side-clip-soft"><rect x="90" y="110" width="1020" height="345" rx="40"/></clipPath>
    </defs>
    <rect class="vehicle-side" x="90" y="110" width="1020" height="345" rx="40"/>
    <g clip-path="url(#side-clip-soft)">
      <polygon class="wrap-field" points="90,210 855,448 855,460 90,460"/>
      <text class="brand-name" x="176" y="218" textLength="690" lengthAdjust="spacingAndGlyphs" transform="rotate(19 176 218)">Brightvane</text>
    </g>
    <g class="contact-block" transform="rotate(18.5 148 247)">
      <circle class="contact-icon" cx="147" cy="242" r="5"/>
      <line class="contact-icon-mark" x1="144" y1="242" x2="150" y2="242"/>
      <text class="contact-line" x="157" y="247">name@brightvane.com</text>
      <circle class="contact-icon" cx="312" cy="242" r="5"/>
      <path class="contact-icon-mark" d="M310 240 q1 4 4 4"/>
      <text class="contact-line" x="322" y="247">000-000-0000</text>
      <circle class="contact-icon" cx="430" cy="242" r="5"/>
      <ellipse class="contact-icon-mark" cx="430" cy="242" rx="2" ry="4"/>
      <text class="contact-line" x="440" y="247">www.brightvane.com</text>
      <text class="contact-line" x="204" y="268">installations and electrical works</text>
    </g>
  </svg>

  <svg class="wrap-variant variant-bright" viewBox="0 0 1190 600" aria-label="Brightvane van wrap, side view, bright yellow version">
    <defs>
      <clipPath id="side-clip-bright"><rect x="90" y="110" width="1020" height="345" rx="40"/></clipPath>
    </defs>
    <rect class="vehicle-side" x="90" y="110" width="1020" height="345" rx="40"/>
    <g clip-path="url(#side-clip-bright)">
      <polygon class="wrap-field" points="90,210 855,448 855,460 90,460"/>
      <text class="brand-name" x="176" y="218" textLength="690" lengthAdjust="spacingAndGlyphs" transform="rotate(19 176 218)">Brightvane</text>
    </g>
    <g class="contact-block" transform="rotate(18.5 148 247)">
      <circle class="contact-icon" cx="147" cy="242" r="5"/>
      <line class="contact-icon-mark" x1="144" y1="242" x2="150" y2="242"/>
      <text class="contact-line" x="157" y="247">name@brightvane.com</text>
      <circle class="contact-icon" cx="312" cy="242" r="5"/>
      <path class="contact-icon-mark" d="M310 240 q1 4 4 4"/>
      <text class="contact-line" x="322" y="247">000-000-0000</text>
      <circle class="contact-icon" cx="430" cy="242" r="5"/>
      <ellipse class="contact-icon-mark" cx="430" cy="242" rx="2" ry="4"/>
      <text class="contact-line" x="440" y="247">www.brightvane.com</text>
      <text class="contact-line" x="204" y="268">installations and electrical works</text>
    </g>
  </svg>

</main>
</body>
</html>
```